Layout for new page on existing website

We have an existing website (www.brightmillworks.org) and need a new page designing to promote a new product.
The new page needs to be consistent with the existing website look and feel (www.brightmillworks.org) but current persistent elements on the standard page design can be moved/removed from the page to accommodate a new layout necessary for getting all the content laid out in a logical user friendly way.
The content required for the page is attached along with a wireframe mock up that may help understand the expectation, however the wireframe was just created to help me work out what was needed on the page and the layout can be different. A key element is the quality of the design of each of the artifacts (e.g. the panel the embedded video needs to go in, icons etc) and a clear display of the information.
Updates
The website that the new page needs to fit into is www.brightmillworks.org, i will also added the company logo to the brief.
Our Corporate Colours
- Green: #A2FF00
- Cream: #FFFF99
- Yellow: #FFE900
- Grey: #534741

```html
<!DOCTYPE html>
<html lang="en">
<head>
<meta charset="utf-8">
<title>Brightmill Works – Course Management and Booking Simplified</title>
<link rel="stylesheet" href="https://fonts.googleapis.com/css2?family=Cuprum:wght@400;700&family=PT+Sans:ital,wght@0,400;0,700;1,400&display=swap">
<style>
  :root {
    --page-bg: #665851;
    --panel: #ffffff;
    --nav-bg: #e9e9e9;
    --nav-divider: #d8d8d8;
    --nav-text: #5a4f49;
    --nav-active: #8cc41a;
    --brand-green: #a2ff00;
    --heading-grey: #a29b96;
    --body-text: #4d4d4d;
    --rule: #dddddd;
    --white: #ffffff;
    --icon-grey: #8a8a8a;
    --video-dark: #1b1b1b;
  }
  * { box-sizing: border-box; margin: 0; padding: 0; }
  html, body { width: 1200px; height: 900px; overflow: hidden; }
  body { background: var(--page-bg); position: relative; font-family: Arial, Helvetica, sans-serif; }

  .brand { position: absolute; left: 160px; top: 28px; display: flex; align-items: center; gap: 12px; }
  .brand-dot { width: 34px; height: 34px; border-radius: 50%; background: var(--brand-green); }
  .brand-name { font-family: "PT Sans", sans-serif; font-weight: 700; font-size: 22px; letter-spacing: 4px; color: var(--white); }

  .join { position: absolute; left: 910px; top: 42px; display: flex; align-items: center; gap: 7px; }
  .join-label { font-family: "Cuprum", sans-serif; font-size: 15px; color: var(--white); margin-right: 5px; }
  .social { width: 20px; height: 20px; border-radius: 3px; background: var(--icon-grey); }

  .panel { position: absolute; left: 150px; top: 96px; width: 900px; height: 691px; background: var(--panel); border-radius: 10px; overflow: hidden; }
  .nav { height: 35px; background: var(--nav-bg); display: flex; list-style: none; }
  .nav li { font-family: "Cuprum", sans-serif; font-weight: 700; font-size: 15px; color: var(--nav-text); padding: 0 11px; line-height: 37px; border-right: 1px solid var(--nav-divider); text-transform: uppercase; }
  .nav li.active { color: var(--nav-active); }

  .hero-art { position: absolute; left: 20px; top: 64px; width: 260px; height: 215px; background: linear-gradient(135deg, #ffffff, #eeeeee 60%, #e2d8d0); border-radius: 2px; }
  .hero-title { position: absolute; left: 284px; top: 64px; font-family: "PT Sans", sans-serif; font-size: 52px; line-height: 54px; color: var(--heading-grey); font-weight: 400; }
  .hero-copy { position: absolute; left: 287px; top: 183px; width: 596px; font-size: 12px; line-height: 18px; color: var(--body-text); }

  .column { position: absolute; top: 298px; width: 420px; border-top: 1px solid var(--rule); }
  .column.left { left: 20px; }
  .column.right { left: 460px; }
  .column h2 { font-family: "PT Sans", sans-serif; font-style: italic; font-weight: 400; font-size: 22px; color: var(--heading-grey); margin-top: 15px; }

  .video { position: absolute; left: 21px; top: 352px; width: 419px; height: 305px; background: linear-gradient(90deg, var(--video-dark) 52%, #2b6d8e 52%, #3f7f5a); border: 3px solid #333; }

  .testimonial { position: absolute; left: 463px; width: 417px; font-size: 12.5px; line-height: 18px; color: var(--body-text); text-align: justify; }
  .testimonial cite { display: block; text-align: right; font-style: italic; color: #777; margin-top: 10px; padding-right: 4px; }
  .testimonial cite span { display: block; text-decoration: underline; }

  .features-title { position: absolute; left: 169px; top: 814px; font-family: "PT Sans", sans-serif; font-size: 30px; color: var(--white); font-weight: 400; }
  .feature { position: absolute; top: 857px; width: 420px; height: 80px; background: var(--panel); border-radius: 10px; }
  .feature.left { left: 170px; }
  .feature.right { left: 610px; }
  .feature-icon { position: absolute; left: 20px; top: 16px; }
  .feature h3 { position: absolute; left: 80px; top: 8px; font-family: "Cuprum", sans-serif; font-weight: 700; font-size: 20px; color: #8a817b; }
  .feature p { position: absolute; left: 80px; top: 36px; font-size: 12px; color: var(--body-text); }
</style>
</head>
<body>
  <header>
    <div class="brand"><span class="brand-dot"></span><span class="brand-name">BRIGHTMILL WORKS</span></div>
    <div class="join">
      <span class="join-label">JOIN US:</span>
      <span class="social" aria-label="Social link"></span>
      <span class="social" aria-label="Social link"></span>
      <span class="social" aria-label="News feed"></span>
    </div>
  </header>

  <main class="panel">
    <ul class="nav">
      <li class="active">Home</li>
      <li>About Us</li>
      <li>Our Services</li>
      <li>Portfolio</li>
      <li>Testimonials</li>
      <li>Contact Us</li>
    </ul>

    <div class="hero-art" role="img" aria-label="Hand-drawn success diagram: mentor, motivate, coach, inspire, teach, team work, vision, lead by example"></div>
    <h1 class="hero-title">Course Management and<br>Booking Simplified</h1>
    <p class="hero-copy">We focus on you, delivering as early as possible so you are able to benefit from your ideas quickly, we do this with passion, pride, creativity and a conscience at a price that will make you smile. We are an honest, ethical and hard working team who push hard to deliver the best for our clients in a fun, interactive and creative environment. If we are able to help you in anyway, we will. You are the reason why we exist, we get a kick out of solving your problems or being part of your vision.</p>

    <section class="column left"><h2>Build with only your business in mind</h2></section>
    <section class="column right"><h2>Testimonials</h2></section>

    <div class="video" role="img" aria-label="Embedded product video player"></div>

    <blockquote class="testimonial" style="top:350px">
      "Working with Brightmill Works brought a professional approach to our development process resulting in high quality software without the high cost and with the added bonus of working with some of the most dedicated people in the business, despite the timezone differences."
      <cite>Owen Calder, Founder<span>www.tallyledger.com</span></cite>
    </blockquote>

    <blockquote class="testimonial" style="top:496px">
      "Thanks to Brightmill Works our company has an exceptional website that is so easy to navigate around. Our customers love it and find it easy to use. Brightmill Works made the process simple to do and helped to launch us in a unique and practical way.<br>We will continue to work with them, helping our company embrace the lucrative space of social networking and advising us on getting the best out of the web"
      <cite>Rhea Dunmore, Director<span>www.stridementor.org.uk</span></cite>
    </blockquote>
  </main>

  <h2 class="features-title">Key Features</h2>
  <article class="feature left">
    <svg class="feature-icon" width="44" height="44" viewBox="0 0 44 44"><circle cx="22" cy="22" r="20" fill="#e6e6e6"/><circle cx="22" cy="22" r="12" fill="#8cc41a"/><circle cx="22" cy="22" r="5" fill="#fff"/></svg>
    <h3>We build web-based applications.</h3>
    <p>We plan, build and support every part of your</p>
  </article>
  <article class="feature right">
    <svg class="feature-icon" width="44" height="44" viewBox="0 0 44 44"><circle cx="22" cy="22" r="20" fill="#e6e6e6"/><circle cx="22" cy="22" r="12" fill="#8cc41a"/><circle cx="22" cy="22" r="5" fill="#fff"/></svg>
    <h3>We build web-based applications.</h3>
    <p>We plan, build and support every part of your</p>
  </article>
</body>
</html>
```